Brightwell Surface Care - Business Card Design

Use company logo and design a new business card. We are looking for a front and back design. The back should be a dark purple background. We want the back to show cartoon-like soap bubbles chasing mildew cartoon shaped figures. This gives the idea that Brightwell Surface Care provides exterior washing services that work. No mildew stands a chance when Brightwell Surface Care shows up to work. The mildew cartoon images should be green in color, have eyes, and look scared of the bubbles. The bubbles should be light blue in color and have eyes that looked excited to be there.
We will advertise on Mingleport and Pixelvine. These Mingleport and Pixelvine icons should be somewhere on the card.

```html
<!DOCTYPE html>
<html lang="en">
<head>
<meta charset="utf-8">
<title>Brightwell Surface Care – Business Card</title>
<link rel="stylesheet" href="https://fonts.googleapis.com/css2?family=Arimo&family=Source+Sans+3:wght@400;600&display=swap">
<style>
  :root {
    --board-bg: #ffffff;
    --board-edge: #e6e6e6;
    --ink-dark: #2b2b2b;
    --label-purple: #5b3f8c;
    --brand-purple: #3d2a5e;
    --social-purple: #4f3b85;
    --back-bg: #3f2a5c;
    --front-bg: #ffffff;
    --bubble-blue: #cbe6f7;
    --bubble-teal: #cfe9e3;
    --water-light: #bfe4f7;
    --water-deep: #1aa3e3;
    --mildew-green: #3c6a5e;
    --back-bubbles: #5a3f82;
    --white: #ffffff;
  }
  * { box-sizing: border-box; margin: 0; padding: 0; }
  html, body { width: 1200px; height: 502px; overflow: hidden; background: var(--board-bg); }
  .board { position: relative; width: 1200px; height: 502px; border: 1px solid var(--board-edge); font-family: "Source Sans 3", sans-serif; }
  .size-title { position: absolute; top: 55px; width: 538px; text-align: center; font-family: "Arimo", sans-serif; font-size: 33px; color: var(--ink-dark); }
  .side-label { position: absolute; top: 455px; width: 538px; text-align: center; font-size: 18px; color: var(--label-purple); }
  .card { position: absolute; top: 105px; width: 538px; height: 340px; overflow: hidden; }
  .card--front { left: 47px; background: var(--front-bg); border: 1px solid #d8d8d8; }
  .card--back { left: 613px; background: var(--back-bg); border: 1px solid #2a1c3e; }
  .art { position: absolute; }
  .front-bubbles { left: 20px; top: 0; width: 500px; height: 250px;
    background: radial-gradient(ellipse at 30% 45%, var(--bubble-blue) 0%, rgba(203,230,247,0.5) 45%, transparent 70%),
                radial-gradient(ellipse at 72% 40%, var(--bubble-teal) 0%, rgba(207,233,227,0.5) 45%, transparent 70%); }
  .front-water { left: 0; top: 170px; width: 538px; height: 170px;
    background: linear-gradient(180deg, rgba(191,228,247,0) 0%, var(--water-light) 35%, #8fd0f0 70%, var(--water-deep) 100%); }
  .back-bubbles { left: 0; top: 0; width: 300px; height: 340px;
    background: radial-gradient(ellipse at 45% 50%, var(--back-bubbles) 0%, rgba(90,63,130,0.4) 55%, transparent 80%); }
  .back-mildew { left: 270px; top: 20px; width: 268px; height: 320px;
    background: radial-gradient(ellipse at 55% 50%, var(--mildew-green) 0%, rgba(60,106,94,0.45) 55%, transparent 80%); }
  .contact { position: absolute; right: 132px; top: 124px; text-align: right; color: var(--brand-purple); }
  .contact__name { font-weight: 600; font-size: 18px; line-height: 20px; }
  .contact__phone { font-size: 18px; line-height: 22px; }
  .brand { position: absolute; font-weight: 600; line-height: 1; }
  .brand--front { left: 100px; top: 168px; color: var(--brand-purple); }
  .brand--front .brand__main { font-size: 64px; letter-spacing: -1px; }
  .brand--front .brand__sub { font-size: 20px; margin-top: 6px; letter-spacing: 1px; }
  .brand--back { left: 210px; top: 240px; color: var(--white); }
  .brand--back .brand__main { font-size: 34px; }
  .brand--back .brand__sub { font-size: 11px; margin-top: 3px; letter-spacing: 1px; }
  .social { position: absolute; display: flex; align-items: center; gap: 5px; font-size: 12px; }
  .social__lead { font-size: 15px; margin-right: 2px; }
  .social__item { display: flex; align-items: center; gap: 3px; }
  .social__dot { width: 9px; height: 9px; border-radius: 50%; background: currentColor; }
  .social--front { right: 36px; top: 292px; color: var(--social-purple); }
  .social--back { right: 14px; top: 310px; color: var(--white); }
</style>
</head>
<body>
<div class="board">
  <div class="size-title" style="left:47px">85.6 mmX 53.98 mm</div>
  <div class="size-title" style="left:613px">85.6 mmX 53.98 mm</div>

  <section class="card card--front">
    <div class="art front-bubbles" role="img" aria-label="Light blue smiling bubbles chasing pale green worried mildew figures"></div>
    <div class="art front-water" role="img" aria-label="Splashing blue water wave with foam bubbles"></div>
    <div class="contact">
      <div class="contact__name">Ravindra Kumar Mehta</div>
      <div class="contact__phone">+91 09876543210</div>
    </div>
    <div class="brand brand--front">
      <div class="brand__main">Brightwell</div>
      <div class="brand__sub">SURFACE CARE</div>
    </div>
    <div class="social social--front">
      <span class="social__lead">Follow us on</span>
      <span class="social__item"><span class="social__dot"></span>Mingleport</span>
      <span class="social__item"><span class="social__dot"></span>Pixelvine</span>
    </div>
  </section>

  <section class="card card--back">
    <div class="art back-bubbles" role="img" aria-label="Purple outlined smiling soap bubbles"></div>
    <div class="art back-mildew" role="img" aria-label="Green outlined scared mildew figures"></div>
    <div class="brand brand--back">
      <div class="brand__main">Brightwell</div>
      <div class="brand__sub">SURFACE CARE</div>
    </div>
    <div class="social social--back">
      <span class="social__lead">Follow us on</span>
      <span class="social__item"><span class="social__dot"></span>Mingleport</span>
      <span class="social__item"><span class="social__dot"></span>Pixelvine</span>
    </div>
  </section>

  <div class="side-label" style="left:47px">FRONT</div>
  <div class="side-label" style="left:613px">BACK</div>
</div>
</body>
</html>
```